High end Desks & Chairs Distibutor looking for a brochure desin

Harbor Loom G.P, Canadian Furniture and Stationery Distributor, (very attractive patented design -mainly Desks & Chairs-), Adjstable to fit many needs.
3 folds flyer,
Bilangual text and photos provided,
Use same colors as Logo
Flyer Disign shoul reflect Ergonomy, High End User Freindly Products, Eco Freindly materials,

Target Market(s)

Limited mobility people
Children from 4 to 17 years old
Multi porpuses desks users

Industry/Entity Type

Distributor

Requirements
Nice to have
• Have a hint for Ergonomic, Adjustable, multi-purpose use.

```html
<!DOCTYPE html>
<html lang="en">
<head>
<meta charset="utf-8">
<title>Harbor Loom Tri-fold Brochure</title>
<link rel="stylesheet" href="https://fonts.googleapis.com/css2?family=Lato:wght@400;700;900&family=Oswald:wght@500;600;700&display=swap">
<style>
  :root {
    --maroon: #8c1d52;
    --gold: #f4b21b;
    --ink: #222222;
    --ink-soft: #4a4a4a;
    --paper: #ffffff;
    --night: #161616;
    --photo-warm: #e9e2d6;
    --photo-cool: #dfe3e8;
  }
  * { margin: 0; padding: 0; box-sizing: border-box; }
  html, body { width: 907px; height: 1200px; overflow: hidden; }
  body { background: var(--paper); font-family: "Lato", sans-serif; color: var(--ink); position: relative; }

  .sheet { position: absolute; left: 109px; width: 690px; height: 491px; overflow: hidden; background: var(--paper); box-shadow: 0 2px 8px rgba(0,0,0,.18); }
  .sheet--outer { top: 88px; }
  .sheet--inner { top: 634px; }
  .sheet__art { position: absolute; inset: 0; }
  .abs { position: absolute; }

  .fold { position: absolute; top: 0; width: 1px; height: 100%; background: rgba(0,0,0,.08); }

  .feature { position: absolute; top: 36px; width: 110px; text-align: center; }
  .feature__icon { width: 36px; height: 36px; margin: 0 auto 6px; }
  .feature__title { font-weight: 900; font-size: 12px; letter-spacing: .2px; color: var(--ink); }
  .feature__sub { font-size: 7px; color: var(--ink); text-transform: uppercase; }

  .we-are__title { left: 17px; top: 120px; font-family: "Oswald", sans-serif; font-weight: 600; font-size: 17px; color: var(--maroon); }
  .we-are__list { left: 22px; top: 152px; width: 190px; list-style: none; font-size: 8px; line-height: 11px; color: var(--ink); }
  .we-are__list li { position: relative; padding-left: 9px; margin-bottom: 8px; }
  .we-are__list li::before { content: ""; position: absolute; left: 0; top: 4px; width: 4px; height: 4px; border-radius: 50%; background: var(--maroon); }

  .photo { position: absolute; }

  .brand { position: absolute; display: flex; align-items: center; gap: 5px; font-family: "Lato", sans-serif; font-weight: 900; color: var(--maroon); }
  .brand__mark { width: 9px; height: 9px; background: var(--maroon); }
  .brand--light { color: var(--paper); }
  .brand--light .brand__mark { background: var(--paper); }

  .badge { position: absolute; left: 276px; top: 215px; width: 150px; height: 150px; border-radius: 50%; background: var(--paper); border: 6px solid var(--gold); display: flex; flex-direction: column; align-items: center; justify-content: center; text-align: center; }
  .badge__lead { font-family: "Oswald", sans-serif; font-weight: 600; font-size: 17px; color: var(--gold); line-height: 1.05; }
  .badge__mid { font-family: "Lato", sans-serif; font-size: 17px; color: var(--ink); line-height: 1.15; }
  .badge__tail { font-family: "Oswald", sans-serif; font-weight: 600; font-size: 16px; color: var(--maroon); line-height: 1.15; letter-spacing: .5px; }

  .phone { left: 237px; width: 226px; top: 415px; text-align: center; font-family: "Oswald", sans-serif; font-weight: 500; font-size: 25px; color: var(--paper); letter-spacing: .5px; }
  .web { width: 226px; top: 452px; text-align: center; font-size: 9.5px; letter-spacing: 2px; color: var(--paper); }

  .cover-title { left: 463px; width: 227px; top: 312px; text-align: center; }
  .cover-title__a { font-family: "Oswald", sans-serif; font-weight: 600; font-size: 46px; line-height: 1; color: var(--gold); letter-spacing: .5px; }
  .cover-title__b { font-family: "Oswald", sans-serif; font-weight: 600; font-size: 37px; line-height: 1.05; color: var(--paper); letter-spacing: .5px; }
  .cover-title__c { font-size: 15px; color: var(--paper); margin-top: 2px; }

  .copy { position: absolute; width: 190px; font-size: 8.3px; line-height: 10.7px; }
  .copy p { margin-bottom: 10px; }
  .copy--dark { color: var(--ink); }
  .copy--light { color: var(--paper); }

  .bullets { position: absolute; display: flex; gap: 8px; width: 200px; font-size: 8px; line-height: 10.5px; }
  .bullets ul { list-style: none; width: 100px; }
  .bullets li { position: relative; padding-left: 8px; margin-bottom: 3px; }
  .bullets li::before { content: ""; position: absolute; left: 0; top: 3px; width: 4px; height: 4px; border-radius: 50%; background: var(--maroon); }
  .bullets--light { color: var(--paper); }
  .bullets--light li::before { background: var(--paper); }
</style>
</head>
<body>

<!-- Outer side -->
<section class="sheet sheet--outer" aria-label="Brochure outer side">
  <svg class="sheet__art" width="690" height="491" viewBox="0 0 690 491" aria-hidden="true">
    <rect x="237" y="0" width="226" height="240" fill="#f6f4f4"/>
    <polygon points="0,404 237,350 237,491 0,491" fill="var(--gold)"/>
    <polygon points="0,414 237,360 237,491 0,491" fill="var(--maroon)"/>
    <polygon points="237,255 463,225 463,491 237,491" fill="var(--maroon)"/>
    <rect x="463" y="262" width="227" height="6" fill="var(--gold)"/>
    <rect x="463" y="268" width="227" height="223" fill="var(--maroon)"/>
  </svg>
  <div class="fold" style="left:237px"></div>
  <div class="fold" style="left:463px"></div>

  <div class="feature" style="left:6px">
    <svg class="feature__icon" viewBox="0 0 36 36" aria-hidden="true">
      <circle cx="18" cy="18" r="17" fill="var(--maroon)" stroke="#d9b3c6" stroke-width="1.5"/>
      <path d="M10 12h3l2.5 9h9l2-6H14" fill="none" stroke="#fff" stroke-width="1.6" stroke-linejoin="round"/>
      <circle cx="16.5" cy="24.5" r="1.3" fill="#fff"/><circle cx="23.5" cy="24.5" r="1.3" fill="#fff"/>
    </svg>
    <div class="feature__title">HIGH END</div>
    <div class="feature__sub">User freindly products</div>
  </div>
  <div class="feature" style="left:121px">
    <svg class="feature__icon" viewBox="0 0 36 36" aria-hidden="true">
      <circle cx="18" cy="18" r="17" fill="var(--maroon)" stroke="#d9b3c6" stroke-width="1.5"/>
      <circle cx="18" cy="13.5" r="4" fill="#fff"/><circle cx="13.5" cy="21" r="4" fill="#fff"/><circle cx="22.5" cy="21" r="4" fill="#fff"/>
    </svg>
    <div class="feature__title">ECO FREINDLY</div>
    <div class="feature__sub">Materials</div>
  </div>

  <h2 class="abs we-are__title">WE ARE</h2>
  <ul class="abs we-are__list">
    <li>Harbor Loom G.P,</li>
    <li>Canadian Furniture and Stationery Distributor (very attractive patented design -mainly Desks &amp; Chairs-)</li>
    <li>Adjstable to fit many needs.</li>
  </ul>

  <div class="photo" role="img" aria-label="Photo of a height-adjustable tilting desk with wooden top on a white pedestal base" style="left:42px;top:240px;width:180px;height:240px;background:linear-gradient(180deg,#e3c28f 0%,#d9b27a 18%,#eeeeee 40%,#dcdcdc 100%);border-radius:6px;opacity:.92"></div>

  <div class="brand" style="left:300px;top:140px;font-size:15px"><span class="brand__mark"></span>Harbor Loom</div>

  <div class="badge">
    <div class="badge__lead">VERY ATTRACTIVE</div>
    <div class="badge__mid">patented design</div>
    <div class="badge__tail">MAINLY</div>
    <div class="badge__tail">DESKS &amp; CHAIRS</div>
  </div>

  <div class="abs phone">0123456789</div>
  <div class="abs web" style="left:237px">www.companywebsite.com</div>

  <div class="brand" style="left:516px;top:60px;font-size:18px"><span class="brand__mark"></span>Harbor Loom</div>
  <div class="photo" role="img" aria-label="Photo of a parent and two children working at an adjustable kids' desk in a bright playroom" style="left:463px;top:78px;width:227px;height:184px;background:linear-gradient(135deg,#d8e4ea 0%,#efe7dc 45%,#cfd8c4 100%)"></div>

  <div class="abs cover-title">
    <div class="cover-title__a">CANADIAN</div>
    <div class="cover-title__b">FURNITURE</div>
    <div class="cover-title__c">and Stationery Distributor</div>
  </div>
  <div class="abs web" style="left:463px">www.companywebsite.com</div>
</section>

<!-- Inner side -->
<section class="sheet sheet--inner" aria-label="Brochure inner side">
  <svg class="sheet__art" width="690" height="491" viewBox="0 0 690 491" aria-hidden="true">
    <polygon points="0,256 463,90 463,464 0,464" fill="var(--maroon)"/>
    <polygon points="0,266 463,100 463,464 0,464" fill="var(--gold)"/>
    <rect x="463" y="110" width="227" height="6" fill="var(--gold)"/>
    <rect x="463" y="116" width="227" height="348" fill="var(--maroon)"/>
    <rect x="0" y="464" width="690" height="27" fill="var(--night)"/>
  </svg>
  <div class="fold" style="left:237px"></div>
  <div class="fold" style="left:463px"></div>

  <div class="photo" role="img" aria-label="Photos of a tilting drafting desk and a two-level adjustable desk" style="left:8px;top:60px;width:225px;height:150px;background:linear-gradient(180deg,var(--photo-cool) 0%,#eef0f2 60%,#d6dade 100%);border-radius:6px"></div>
  <div class="photo" role="img" aria-label="Photos of an adjustable student desk and a standing-height desk shown with a height guide" style="left:245px;top:6px;width:215px;height:150px;background:linear-gradient(180deg,#eef0f3 0%,var(--photo-cool) 100%);border-radius:6px"></div>
  <div class="photo" role="img" aria-label="Photos of a white adjustable desk and a desk with pull-out drawers" style="left:470px;top:20px;width:214px;height:82px;background:linear-gradient(180deg,#f1f2f3 0%,var(--photo-cool) 100%);border-radius:6px"></div>

  <div class="copy copy--dark" style="left:23px;top:275px">
    <p>Et est putent contentiones. No mel nullam vocent reformidans, pro ea audiam denique, fabulas molestiae eu mel. Cu rebum doming mea, molestiae eloquentiam appellantur no sit. Ut graeco denique vix, solum error lucilius ei his, eam sumo zril tincidunt an. At vis novum accumsan facilisis, sit ex laudem aperiri delicata, brute mazim eripuit duo at.</p>
  </div>
  <div class="bullets" style="left:23px;top:357px">
    <ul><li>Eu nam reque atqui mea ad nostrud perfecto</li><li>Partem quaeque omittantur cu ius</li><li>Ea has habemus appellantur</li><li>Omnes soluta quaerendum his an</li></ul>
    <ul><li>Eum deleniti luptatum rationibus eu</li><li>No sea odio eligendi Mel ei nihil homero</li><li>Eu numquam alienum omittam duo</li><li>Feugait repudiandae signiferumque est an</li></ul>
  </div>

  <div class="copy copy--dark" style="left:247px;top:196px;width:200px">
    <p>Eu nam reque atqui, mea ad nostrud perfecto. Partem quaeque omittantur cu ius, ea has habemus appellantur. Omnes soluta quaerendum his an, eum deleniti luptatum rationibus eu, no sea odio eligendi. Mel ei nihil homero, eu numquam alienum omittam duo. Feugait repudiandae signiferumque est an.</p>
    <p>Et est putent contentiones. No mel nullam vocent reformidans, pro ea audiam denique, fabulas molestiae eu mel. Cu rebum doming mea, molestiae eloquentiam appellantur no sit. Ut graeco denique vix, solum error lucilius ei his, eam sumo zril tincidunt an. At vis novum accumsan facilisis, sit ex laudem aperiri delicata, brute mazim eripuit duo at.</p>
  </div>
  <div class="bullets" style="left:247px;top:359px">
    <ul><li>Eu nam reque atqui mea ad nostrud perfecto</li><li>Partem quaeque omittantur cu ius</li><li>Ea has habemus appellantur</li><li>Omnes soluta quaerendum his an</li></ul>
    <ul><li>Eum deleniti luptatum rationibus eu</li><li>No sea odio eligendi Mel ei nihil homero</li><li>Eu numquam alienum omittam duo</li><li>Feugait repudiandae signiferumque est an</li></ul>
  </div>

  <div class="copy copy--light" style="left:477px;top:140px;width:200px">
    <p>Eu nam reque atqui, mea ad nostrud perfecto. Partem quaeque omittantur cu ius, ea has habemus appellantur. Omnes soluta quaerendum his an, eum deleniti luptatum rationibus eu, no sea odio eligendi. Mel ei nihil homero, eu numquam alienum omittam duo. Feugait repudiandae signiferumque est an.</p>
    <p>Et est putent contentiones. No mel nullam vocent reformidans, pro ea audiam denique, fabulas molestiae eu mel. Cu rebum doming mea, molestiae eloquentiam appellantur no sit. Ut graeco denique vix, solum error lucilius ei his, eam sumo zril tincidunt an. At vis novum accumsan facilisis, sit ex laudem aperiri delicata, brute mazim eripuit duo at.</p>
  </div>
  <div class="bullets bullets--light" style="left:477px;top:302px">
    <ul><li>Eu nam reque atqui mea ad nostrud perfecto</li><li>Partem quaeque omittantur cu ius</li><li>Ea has habemus appellantur</li><li>Omnes soluta quaerendum his an</li></ul>
    <ul><li>Eum deleniti luptatum rationibus eu</li><li>No sea odio eligendi Mel ei nihil homero</li><li>Eu numquam alienum omittam duo</li><li>Feugait repudiandae signiferumque est an</li></ul>
  </div>

  <div class="brand brand--light" style="left:530px;top:436px;font-size:14px"><span class="brand__mark"></span>Harbor Loom</div>
</section>

</body>
</html>
```